Real Estate Wordpress Landing Page

I'm looking to a landing page dedicated to my real estate brokerage that's catered to promoting that my company provides 1.5% listings to home sellers... I have a couple examples that I'm really looking towards mocking in a version with similar color schemes using my current company colors/website.

http://lorvanta.com/
https://www.bluthorn.com/about/one-percent-listing-fee

My brokerage company website is http://www.calmridge.us/

Target Market(s)

real estate home sellers & buyers

Industry/Entity Type

Real Estate

Coding

Coded - Design and coding required

Number of Pages Required

1 page

Colors
3176b5
0255a3
eaf1f7
cedeed

Requirements
Must have
• Company website colors - http://www.calmridge.us/
• Something around the lines of this website page - http://lorvanta.com/
• Wordpress compatibility

```html
<!DOCTYPE html>
<html lang="en">
<head>
<meta charset="utf-8">
<title>Calmridge Realty – List for 1.5% Commission</title>
<link rel="stylesheet" href="https://fonts.googleapis.com/css2?family=Montserrat:wght@400;500;600;700;800&family=Open+Sans:wght@400;600;700&display=swap">
<style>
:root{
  --blue:#0255a3;
  --blue-mid:#3176b5;
  --blue-pale:#eaf1f7;
  --blue-soft:#cedeed;
  --navy:#0b2a55;
  --ink:#1d2433;
  --muted:#5a6575;
  --line:#d4dbe4;
  --white:#ffffff;
  --black:#111418;
}
*{box-sizing:border-box;margin:0;padding:0}
html,body{width:1200px;height:4500px;overflow:hidden}
body{font-family:"Open Sans",Arial,sans-serif;color:var(--ink);background:var(--white);position:relative}
.section{position:absolute;left:0;width:1200px}
.container{position:relative;width:900px;margin:0 auto;height:100%}
h1,h2,h3,h4,.display{font-family:"Montserrat",Arial,sans-serif}
.btn{display:inline-block;font-family:"Montserrat",Arial,sans-serif;font-weight:700;color:var(--white);background:var(--blue);border-radius:4px;text-decoration:none;letter-spacing:.5px;white-space:nowrap}
.placeholder{position:absolute}

/* header */
.site-header{top:0;height:96px;background:var(--white)}
.logo{position:absolute;left:0;top:8px;width:130px;height:118px;background:var(--white);z-index:3;display:flex;flex-direction:column;align-items:center;justify-content:center;gap:8px;border-radius:0 0 6px 6px}
.logo-mark{width:46px;height:46px;background:var(--blue)}
.logo-name{font-family:"Montserrat",Arial,sans-serif;font-weight:700;font-size:17px;color:var(--blue)}
.topbar{position:absolute;right:0;top:10px;display:flex;align-items:center;gap:10px;font-size:11px;color:var(--ink);white-space:nowrap}
.topbar .social{display:flex;gap:5px}
.topbar .social span{width:16px;height:16px;border:1px solid var(--muted);border-radius:50%}
.topbar .btn{font-size:11px;padding:7px 14px}
.topbar .icon{display:inline-flex;align-items:center;gap:5px}
.main-nav{top:96px;height:30px;background:var(--blue)}
.main-nav ul{list-style:none;position:absolute;left:170px;top:0;height:30px;display:flex;align-items:center;gap:26px;font-family:"Montserrat",Arial,sans-serif;font-size:12px;font-weight:600;color:var(--white);white-space:nowrap}

/* hero */
.hero{top:126px;height:489px;overflow:hidden}
.hero-photo{left:0;top:0;width:1200px;height:489px;background:linear-gradient(180deg,#6e8fa6 0%,#8aa6a1 35%,#5c7a52 70%,#3f5e3a 100%)}
.hero-content{position:absolute;left:0;right:0;top:180px;text-align:center;color:var(--white)}
.hero-content h1{font-size:36px;font-weight:700;text-shadow:0 2px 6px rgba(0,0,0,.4)}
.hero-content p{font-family:"Montserrat",Arial,sans-serif;font-size:22px;font-weight:600;margin-top:6px;line-height:1.3;text-shadow:0 2px 6px rgba(0,0,0,.4)}
.hero-content .btn{margin-top:20px;font-size:13px;padding:14px 30px}
.hero-dots{position:absolute;left:0;right:0;top:460px;display:flex;justify-content:center;gap:7px;z-index:2}
.hero-dots span{width:8px;height:8px;border-radius:50%;background:rgba(255,255,255,.6)}
.hero-dots span:first-child{background:var(--white)}
.hero-wave{position:absolute;left:0;bottom:0;width:1200px;height:80px}

/* search */
.search{top:615px;height:171px;background:linear-gradient(180deg,#0255a3,#0a4a8e)}
.search-skyline{left:0;bottom:0;width:1200px;height:120px;background:linear-gradient(180deg,rgba(255,255,255,0),rgba(255,255,255,.08))}
.search h2{position:absolute;top:40px;left:0;right:0;text-align:center;color:var(--white);font-size:15px;letter-spacing:5px;font-weight:700}
.search-form{position:absolute;left:245px;top:74px;width:710px;display:flex;gap:6px;align-items:flex-end}
.field{display:flex;flex-direction:column;gap:3px}
.field label{font-size:10px;color:var(--white);font-weight:600;white-space:nowrap}
.field span{display:block;height:24px;background:var(--white);font-size:10px;color:var(--muted);padding:5px 7px;border-radius:2px;white-space:nowrap;overflow:hidden}
.search-form .btn{height:24px;font-size:11px;padding:5px 14px;background:var(--blue-mid)}

/* savings */
.savings{top:786px;height:444px;text-align:center}
.savings h2{position:absolute;left:0;right:0;top:56px;font-size:17px;font-weight:700;color:var(--blue)}
.savings .lead{position:absolute;left:180px;top:84px;width:540px;font-size:12px;line-height:1.5;color:var(--ink)}
.savings h3{position:absolute;left:0;right:0;top:148px;font-size:24px;font-weight:700;color:var(--blue);text-decoration:underline;text-underline-offset:5px}
.saving-side{position:absolute;top:204px;font-size:11px;color:var(--blue)}
.saving-side strong{display:block;font-family:"Montserrat",Arial,sans-serif;font-size:20px;color:var(--ink);font-weight:600}
.saving-side.left{left:0;text-align:left}
.saving-side.right{right:0;text-align:right}
.slider{position:absolute;left:0;right:0;top:262px;height:4px;background:var(--blue-soft)}
.slider::before{content:"";position:absolute;left:0;top:0;width:50%;height:4px;background:var(--blue)}
.slider .knob{position:absolute;left:435px;top:-9px;width:22px;height:22px;background:var(--blue);border-radius:2px}
.slider .end-l,.slider .end-r{position:absolute;top:-6px;width:0;height:0;border-top:8px solid transparent;border-bottom:8px solid transparent}
.slider .end-l{left:-6px;border-right:8px solid var(--blue)}
.slider .end-r{right:-6px;border-left:8px solid var(--blue-soft)}
.total{position:absolute;left:0;right:0;top:302px;font-family:"Montserrat",Arial,sans-serif;font-weight:700;font-size:14px;color:var(--blue)}
.total strong{display:block;font-size:22px;margin-top:2px}
.tagline{position:absolute;left:0;right:0;top:370px;font-size:15px;line-height:20px;color:var(--ink)}
.tagline b{color:var(--blue)}

/* cities */
.cities{top:1254px;height:432px}
.city{position:absolute;color:var(--white);text-align:center;display:flex;flex-direction:column;align-items:center;justify-content:center;gap:4px}
.city h3{font-size:16px;font-weight:600;text-shadow:0 1px 4px rgba(0,0,0,.5)}
.city p{font-size:12px}
.city .btn{font-size:11px;padding:6px 14px;margin-top:4px;background:var(--blue-mid);font-weight:600}
.city-boynton{left:0;top:0;width:384px;height:204px;background:linear-gradient(160deg,#4f6a56,#2f4136)}
.city-delray{left:399px;top:0;width:402px;height:204px;background:linear-gradient(160deg,#6c7b82,#3d4a4f)}
.city-gardens{left:816px;top:0;width:384px;height:432px;background:linear-gradient(180deg,#5a6b60,#3b4a40 60%,#6a5a4a)}
.city-lakeworth{left:0;top:216px;width:801px;height:216px;background:linear-gradient(160deg,#5f7080,#34404c)}

/* promo banner */
.promo{top:1734px;height:150px;background:var(--blue);text-align:center;color:var(--white)}
.promo h2{padding-top:22px;font-size:44px;font-weight:700;letter-spacing:1px}
.promo p{font-family:"Montserrat",Arial,sans-serif;font-size:30px;font-weight:600;margin-top:2px}

/* listings */
.listings{top:1884px;height:411px}
.listings-head{position:absolute;left:9px;top:14px}
.listings-head h2{font-size:20px;font-weight:700;color:var(--ink)}
.listings-head p{font-size:10px;color:var(--muted);text-transform:uppercase}
.arrows{position:absolute;right:12px;top:16px;display:flex;gap:4px}
.arrows span{width:24px;height:24px;background:var(--blue-soft);display:flex;align-items:center;justify-content:center}
.card{position:absolute;top:81px;width:285px;height:300px;background:var(--white)}
.card .photo{position:absolute;left:0;top:0;width:285px;height:150px;background:linear-gradient(180deg,#7fa8c9,#8a9f7a 55%,#5c7b4a)}
.card .badge{position:absolute;left:8px;top:8px;background:#5cae3a;color:var(--white);font-size:8px;font-weight:700;padding:2px 6px}
.card h4{position:absolute;left:0;top:160px;width:285px;font-size:12px;font-weight:700;line-height:1.3;color:var(--ink);text-transform:uppercase}
.card .area{position:absolute;left:0;top:194px;font-size:9px;color:var(--muted);text-transform:uppercase}
.card .specs{position:absolute;left:0;top:212px;width:285px;display:grid;grid-template-columns:1fr 1fr;row-gap:6px;font-size:10px;color:var(--ink)}
.card .specs span::before{content:"";display:inline-block;width:9px;height:7px;background:var(--blue);margin-right:6px}
.card .bar{position:absolute;left:0;top:262px;width:285px;height:28px;display:flex;font-size:10px;font-weight:700;color:var(--white)}
.card .bar .sale{width:100px;background:var(--blue);padding:8px 10px}
.card .bar .price{flex:1;background:var(--black);padding:7px 10px;text-align:right;font-size:12px}
.card-1{left:9px}.card-2{left:309px}.card-3{left:609px}

/* broker */
.broker{top:2310px;height:315px;background:linear-gradient(90deg,#0a2f5e,#12407a 60%,#0a2f5e);color:var(--white)}
.broker-photo{right:150px;top:0;width:210px;height:315px;background:linear-gradient(180deg,#2a4a74,#1a2f4e)}
.broker h2{position:absolute;left:9px;top:52px;font-size:22px;font-weight:700}
.broker .intro{position:absolute;left:9px;top:84px;width:520px;font-size:13px;line-height:1.45}
.broker .cta{position:absolute;left:9px;top:132px;font-family:"Montserrat",Arial,sans-serif;font-size:22px;font-weight:700}
.broker .contacts{position:absolute;left:9px;top:180px;display:flex;gap:48px;font-family:"Montserrat",Arial,sans-serif;font-size:24px;font-weight:600}
.broker .contacts span{display:inline-flex;align-items:center;gap:12px}
.broker .social{position:absolute;left:9px;top:236px;display:flex;gap:8px}
.broker .social span{width:28px;height:28px;border:2px solid var(--white);border-radius:50%}

/* guarantee */
.guarantee{top:2679px;height:126px;background:var(--blue);color:var(--white);text-align:center}
.guarantee p{padding-top:34px;font-family:"Montserrat",Arial,sans-serif;font-size:23px;font-weight:600;line-height:1.35}

/* services */
.services{top:2820px;height:690px}
.service-img{position:absolute;width:432px;height:225px}
.service-text{position:absolute;width:420px}
.service-text h3{font-size:17px;font-weight:700;color:var(--ink);text-transform:uppercase}
.service-text ul{list-style:none;margin-top:12px}
.service-text li{font-size:12px;line-height:2;color:var(--ink);display:flex;align-items:center;gap:8px}
.service-text .btn{margin-top:12px;font-size:11px;padding:8px 16px}
.img-home{left:-3px;top:0;background:linear-gradient(180deg,#7eb3e0,#d8d2c2 55%,#6a9a55)}
.img-room{left:450px;top:234px;background:linear-gradient(160deg,#d7d9dc,#8c8f94 60%,#3d3f44)}
.img-villa{left:-3px;top:456px;background:linear-gradient(180deg,#8fc0e8,#d9d0b8 55%,#5f8a4a)}
.txt-1{left:480px;top:45px}
.txt-2{left:9px;top:279px}
.txt-3{left:480px;top:501px}

/* contact */
.contact{top:3540px;height:420px}
.contact h2{position:absolute;left:9px;top:12px;font-size:18px;font-weight:700;color:var(--ink)}
.contact .intro{position:absolute;left:9px;top:46px;width:880px;font-size:11px;line-height:1.6;color:var(--muted)}
.inputs{position:absolute;left:9px;top:114px;width:880px;display:flex;gap:18px}
.inputs span{flex:1;height:48px;border:1px solid var(--line);border-radius:24px;padding:14px 24px;font-size:13px;color:var(--muted)}
.textarea{position:absolute;left:9px;top:180px;width:880px;height:130px;border:1px solid var(--line);border-radius:14px;padding:22px 24px;font-size:13px;color:var(--muted)}
.contact .submit{position:absolute;left:309px;top:336px;width:280px;height:48px;border-radius:24px;font-size:14px;display:flex;align-items:center;justify-content:center;background:var(--blue)}

/* newsletter */
.newsletter{top:3990px;height:180px;background:linear-gradient(180deg,#0c2346,#132d55);color:var(--white);text-align:center}
.newsletter h2{padding-top:42px;font-size:17px;font-weight:700;letter-spacing:1px}
.newsletter p{font-size:12px;margin-top:8px;opacity:.85}
.subscribe{position:absolute;left:300px;top:100px;width:600px;height:38px;display:flex}
.subscribe span{flex:1;background:var(--white);color:var(--muted);font-size:12px;text-align:left;padding:11px 16px}
.subscribe b{width:160px;background:var(--blue);font-family:"Montserrat",Arial,sans-serif;font-size:12px;padding:11px 0}

/* footer */
.site-footer{top:4170px;height:330px;background:var(--navy);color:var(--white)}
.footer-cols{position:absolute;left:0;top:54px;width:900px;display:grid;grid-template-columns:150px 190px 330px 230px}
.footer-cols h4{font-size:12px;font-weight:700;margin-bottom:16px;text-transform:uppercase}
.footer-cols ul{list-style:none}
.footer-cols li{font-size:11px;line-height:2.4;opacity:.85}
.recent{display:flex;gap:10px;margin-bottom:14px;font-size:10px;line-height:1.4}
.recent .thumb{width:70px;height:44px;background:linear-gradient(180deg,#7ea7c8,#6b8a5a)}
.recent em{font-style:normal;color:#7fb2e5;font-weight:700}
.contact-line{display:flex;gap:10px;align-items:flex-start;font-size:11px;line-height:1.5;margin-bottom:14px}
.contact-line.big{font-family:"Montserrat",Arial,sans-serif;font-size:18px;font-weight:600}
.footer-bottom{position:absolute;left:0;right:0;bottom:0;height:44px;border-top:1px solid rgba(255,255,255,.15)}
.footer-bottom .container{display:flex;align-items:center;justify-content:space-between;font-size:11px;opacity:.85}
.footer-bottom .follow{display:flex;align-items:center;gap:10px}
.footer-bottom .follow span{width:12px;height:12px;border-radius:50%;background:rgba(255,255,255,.6)}
</style>
</head>
<body>

<header class="section site-header">
  <div class="container">
    <div class="logo"><span class="logo-mark"></span><span class="logo-name">Calmridge</span></div>
    <div class="topbar">
      <span class="icon"><svg width="12" height="12" viewBox="0 0 24 24"><path fill="#0255a3" d="M6.6 10.8a15 15 0 0 0 6.6 6.6l2.2-2.2a1 1 0 0 1 1-.25 11.4 11.4 0 0 0 3.6.57 1 1 0 0 1 1 1V20a1 1 0 0 1-1 1A17 17 0 0 1 3 4a1 1 0 0 1 1-1h3.5a1 1 0 0 1 1 1c0 1.25.2 2.45.57 3.6a1 1 0 0 1-.25 1z"/></svg>555-014-7930</span>
      <span class="social"><span></span><span></span><span></span><span></span><span></span></span>
      <span class="icon"><svg width="12" height="10" viewBox="0 0 24 18"><rect x="1" y="1" width="22" height="16" fill="none" stroke="#0255a3" stroke-width="2"/><path d="M1 1l11 9 11-9" fill="none" stroke="#0255a3" stroke-width="2"/></svg>contact@calmridge.us</span>
      <span>Email Alert</span><span>Register</span><span>Login</span>
      <a class="btn">Buy With Us</a><a class="btn">Sale With Us</a>
    </div>
  </div>
</header>

<nav class="section main-nav">
  <div class="container">
    <ul>
      <li>Home</li><li>Featured cities</li><li>Property Search</li><li>Communities</li><li>Rentals</li><li>Investing</li><li>Contact</li><li>Calmridge</li>
      <li><svg width="12" height="12" viewBox="0 0 24 24"><circle cx="10" cy="10" r="7" fill="none" stroke="#fff" stroke-width="3"/><path d="M15 15l7 7" stroke="#fff" stroke-width="3"/></svg></li>
    </ul>
  </div>
</nav>

<section class="section hero">
  <div class="placeholder hero-photo" role="img" aria-label="Photo of a tropical Florida home with palm trees and a sold sign in the front yard"></div>
  <div class="hero-content">
    <h1>Boynton Beach Realtor</h1>
    <p>Discover Some of the Best Communities<br>in Palm Beach County, FL</p>
    <a class="btn">DISCOVER NOW</a>
  </div>
  <div class="hero-dots"><span></span><span></span><span></span><span></span></div>
  <svg class="hero-wave" viewBox="0 0 1200 80" preserveAspectRatio="none"><path d="M0 40 Q300 0 600 30 T1200 20 V80 H0Z" fill="#3176b5" opacity=".7"/><path d="M0 55 Q300 25 600 50 T1200 40 V80 H0Z" fill="#0255a3"/></svg>
</section>

<section class="section search">
  <div class="placeholder search-skyline" role="img" aria-label="Faint city skyline silhouette"></div>
  <h2>SEARCH YOUR PROPERTY</h2>
  <div class="search-form">
    <div class="field" style="width:160px"><label>Location</label><span>City or Zip</span></div>
    <div class="field" style="width:120px"><label>Property Type</label><span>Houses/ Condos</span></div>
    <div class="field" style="width:96px"><label>Min. Price</label><span>Any</span></div>
    <div class="field" style="width:96px"><label>Max. Price</label><span>Any</span></div>
    <div class="field" style="width:62px"><label>Beds</label><span>Any</span></div>
    <div class="field" style="width:62px"><label>Baths</label><span>Any</span></div>
    <a class="btn">Search</a>
  </div>
</section>

<section class="section savings">
  <div class="container">
    <h2>SEE HOW MUCH YOU COULD SAVE WITH CALMRIDGE</h2>
    <p class="lead">Sell with Calmridge and pay only 1.5% listing fee and still receive top marketing. Buy with a Calmridge Agent and we'll give 1% of our commission back to you. Either way, you'll get second to none service and will save thousands $$$!</p>
    <h3>Our Client Savings</h3>
    <div class="saving-side left"><strong>$2698</strong>Calmridge Buyer Saving</div>
    <div class="saving-side right"><strong>$2698</strong>Calmridge Seller Saving</div>
    <div class="slider"><span class="end-l"></span><span class="knob"></span><span class="end-r"></span></div>
    <div class="total">Total Savings When You Use Us:<strong>$ 14,250</strong></div>
    <p class="tagline">LIST FOR <b>1.5% connission</b> And Receive Top Marketing from Real Estate Pro!</p>
  </div>
</section>

<section class="section cities">
  <div class="city city-boynton" role="img" aria-label="Aerial photo of Boynton Beach homes"><h3>Boynton Beach Home</h3><p>225 Listing</p><a class="btn">View Listing</a></div>
  <div class="city city-delray" role="img" aria-label="Photo of Delray Beach homes"><h3>Delray Beach Home</h3><p>405 Listing</p><a class="btn">View Listing</a></div>
  <div class="city city-gardens" role="img" aria-label="Photo of a Palm Beach Gardens home with driveway"><h3>Palm Beach Gardens Homes</h3><p>321 Listing</p><a class="btn">View Listing</a></div>
  <div class="city city-lakeworth" role="img" aria-label="Photo of Lake Worth homes"><h3>Lake Worth Homes</h3><p>812 Listing</p><a class="btn">View Listing</a></div>
</section>

<section class="section promo">
  <h2>LIST FOR 1.5% COMMISSION,</h2>
  <p>And Receive Top Marketing from Real Estate Pro!</p>
</section>

<section class="section listings">
  <div class="container">
    <div class="listings-head"><h2>FEATURED LISTINGS</h2><p>Find your home in your city</p></div>
    <div class="arrows">
      <span><svg width="8" height="10" viewBox="0 0 8 10"><path d="M6 1L2 5l4 4" fill="none" stroke="#0255a3" stroke-width="2"/></svg></span>
      <span><svg width="8" height="10" viewBox="0 0 8 10"><path d="M2 1l4 4-4 4" fill="none" stroke="#0255a3" stroke-width="2"/></svg></span>
    </div>
    <article class="card card-1">
      <div class="photo" role="img" aria-label="Photo of a two-storey home with palm trees"></div><span class="badge">FEATURED</span>
      <h4>2191 Harbor Crest Circle, Royal Palm Beach, FL 33411</h4>
      <p class="area">Madison Green / Parcel C and I</p>
      <div class="specs"><span>3,456 sqft</span><span>5 Bedrooms</span><span>3 bathrooms</span><span>3 Garage</span></div>
      <div class="bar"><span class="sale">FOR SALE</span><span class="price">Price $459,000</span></div>
    </article>
    <article class="card card-2">
      <div class="photo" role="img" aria-label="Photo of a home with palm trees and a lawn"></div><span class="badge">FEATURED</span>
      <h4>1477 Willow Bend Lane, Royal Palm Beach, FL 33411</h4>
      <p class="area">Madison Green</p>
      <div class="specs"><span>2,192 sqft</span><span>4 Bedrooms</span><span>2 bathrooms</span><span>2 Garage</span></div>
      <div class="bar"><span class="sale">FOR SALE</span><span class="price">Price $339,900</span></div>
    </article>
    <article class="card card-3">
      <div class="photo" role="img" aria-label="Photo of a two-storey home with a paved driveway"></div><span class="badge">FEATURED</span>
      <h4>233 Seabreeze Boulevard, Royal Palm Beach, FL 33411</h4>
      <p class="area">Madison Green 1</p>
      <div class="specs"><span>2,693 sqft</span><span>4 Bedrooms</span><span>3 bathrooms</span><span>1 Garage</span></div>
      <div class="bar"><span class="sale">FOR SALE</span><span class="price">Price $355,000</span></div>
    </article>
  </div>
</section>

<section class="section broker">
  <div class="placeholder broker-photo" role="img" aria-label="Portrait photo of the broker in a suit"></div>
  <div class="container">
    <h2>MARCUS DELANE, Lic. Real Estate Broker</h2>
    <p class="intro">On average, our customers save $5,600 when they list with us... and they still receive top marketing and quality professional service!</p>
    <p class="cta">CALL US TODAY AND SAVE THOUSANDS $$$</p>
    <div class="contacts">
      <span><svg width="24" height="24" viewBox="0 0 24 24"><circle cx="12" cy="12" r="11" fill="#fff"/><path fill="#0b2a55" d="M8.4 10.9a9 9 0 0 0 4 4l1.3-1.3a.6.6 0 0 1 .6-.15 7 7 0 0 0 2.2.35.6.6 0 0 1 .6.6v2a.6.6 0 0 1-.6.6A10.2 10.2 0 0 1 6.3 6.8a.6.6 0 0 1 .6-.6h2a.6.6 0 0 1 .6.6c0 .75.12 1.5.35 2.2a.6.6 0 0 1-.15.6z"/></svg>555-019-6902</span>
      <span><svg width="26" height="20" viewBox="0 0 26 20"><rect x="1" y="1" width="24" height="18" fill="#fff"/><path d="M1 1l12 9 12-9" fill="none" stroke="#0b2a55" stroke-width="2"/></svg>www.calmridge.us</span>
    </div>
    <div class="social"><span></span><span></span><span></span><span></span><span></span><span></span></div>
  </div>
</section>

<section class="section guarantee">
  <p>30 Day Listing Service GUARANTEED. Save thousands $$$ listing with us!<br>Morbi eu sem felis. Integer faucibus ligula vitae enim vestibulum iaculis.</p>
</section>

<section class="section services">
  <div class="container">
    <div class="service-img img-home" role="img" aria-label="Photo of a two-storey home with a garage"></div>
    <div class="service-text txt-1">
      <h3>Seal with Calmridge &amp; Save $$$</h3>
      <ul><li><svg width="10" height="10" viewBox="0 0 10 10"><path d="M1 5l3 3 5-6" fill="none" stroke="#0255a3" stroke-width="2"/></svg>Professional Real Estate Photography</li><li><svg width="10" height="10" viewBox="0 0 10 10"><path d="M1 5l3 3 5-6" fill="none" stroke="#0255a3" stroke-width="2"/></svg>Complimentary Comparative Market Analysis (CMA)</li><li><svg width="10" height="10" viewBox="0 0 10 10"><path d="M1 5l3 3 5-6" fill="none" stroke="#0255a3" stroke-width="2"/></svg>FREE Consultation with Real Estate Professional</li></ul>
      <a class="btn">CALL US ! &nbsp; 555-019-6902</a>
    </div>
    <div class="service-text txt-2">
      <h3>Start Your Home Search With Us</h3>
      <ul><li><svg width="10" height="10" viewBox="0 0 10 10"><path d="M1 5l3 3 5-6" fill="none" stroke="#0255a3" stroke-width="2"/></svg>1% Buyer Credit at Closing from Calmridge Realty</li><li><svg width="10" height="10" viewBox="0 0 10 10"><path d="M1 5l3 3 5-6" fill="none" stroke="#0255a3" stroke-width="2"/></svg>Quis Molestie Turpis Dapibus At</li><li><svg width="10" height="10" viewBox="0 0 10 10"><path d="M1 5l3 3 5-6" fill="none" stroke="#0255a3" stroke-width="2"/></svg>Quis Molestie Turpis Dapibus At</li></ul>
      <a class="btn">CALL US ! &nbsp; 555-019-6902</a>
    </div>
    <div class="service-img img-room" role="img" aria-label="Photo of a bright modern living room"></div>
    <div class="service-img img-villa" role="img" aria-label="Photo of a cream two-storey villa with a lawn"></div>
    <div class="service-text txt-3">
      <h3>Leasing &amp; Property Management</h3>
      <ul><li><svg width="10" height="10" viewBox="0 0 10 10"><path d="M1 5l3 3 5-6" fill="none" stroke="#0255a3" stroke-width="2"/></svg>We can manage your rental portfolio for you!</li><li><svg width="10" height="10" viewBox="0 0 10 10"><path d="M1 5l3 3 5-6" fill="none" stroke="#0255a3" stroke-width="2"/></svg>Professional &amp; Experienced Property Managers</li><li><svg width="10" height="10" viewBox="0 0 10 10"><path d="M1 5l3 3 5-6" fill="none" stroke="#0255a3" stroke-width="2"/></svg>Receive Top Dollar for your Rental Properties</li></ul>
      <a class="btn">CALL US ! &nbsp; 555-019-6902</a>
    </div>
  </div>
</section>

<section class="section contact">
  <div class="container">
    <h2>GET IN TOUCH WITH US</h2>
    <p class="intro">We offer our clients a wealth of knowledge regarding all aspects of purchasing or selling a home. Whether it is helping you search for your dream home, discussing new Florida real estate developments, or assisting with the sale of your property, we would love the opportunity to help. Please feel free to contact us with any questions!</p>
    <div class="inputs"><span>Name</span><span>Email</span><span>Phone</span></div>
    <div class="textarea">Your Message</div>
    <a class="btn submit">SUBMIT NOW</a>
  </div>
</section>

<section class="section newsletter">
  <h2>SUBSCRIBE OUR NEWSLETTER</h2>
  <p>Enter your email address to receive our news and updates in your inbox</p>
  <div class="subscribe"><span>Your Email</span><b>SUBSCRIBE NOW</b></div>
</section>

<footer class="section site-footer">
  <div class="container">
    <div class="footer-cols">
      <div><h4>Quick Links</h4><ul><li>Home</li><li>About</li><li>Services</li><li>Blog</li></ul></div>
      <div><h4>Other Links</h4><ul><li>Privacy</li><li>Terms and Conditions</li><li>Contact Us</li><li>Mobile Notary</li></ul></div>
      <div><h4>Recent Properties</h4>
        <div class="recent"><span class="thumb" role="img" aria-label="Thumbnail photo of a home"></span><span>1180 Palm Ave E<br>Lakeside, FL 33411<br><em>$235,000</em></span></div>
        <div class="recent"><span class="thumb" role="img" aria-label="Thumbnail photo of a home"></span><span>4420 Coral Rd E<br>Lakeside, FL 33411<br><em>$235,000</em></span></div>
      </div>
      <div><h4>Contact With Us</h4>
        <div class="contact-line"><svg width="12" height="16" viewBox="0 0 12 16"><path d="M6 0a6 6 0 0 1 6 6c0 4.5-6 10-6 10S0 10.5 0 6a6 6 0 0 1 6-6z" fill="#fff"/><circle cx="6" cy="6" r="2.2" fill="#0b2a55"/></svg><span>4120 Meadow Row<br>Lakeside, WA 98000</span></div>
        <div class="contact-line"><svg width="14" height="11" viewBox="0 0 26 20"><rect x="1" y="1" width="24" height="18" fill="#fff"/><path d="M1 1l12 9 12-9" fill="none" stroke="#0b2a55" stroke-width="2"/></svg><span>contact@calmridge.us</span></div>
        <div class="contact-line big"><svg width="16" height="16" viewBox="0 0 24 24"><path fill="#fff" d="M6.6 10.8a15 15 0 0 0 6.6 6.6l2.2-2.2a1 1 0 0 1 1-.25 11.4 11.4 0 0 0 3.6.57 1 1 0 0 1 1 1V20a1 1 0 0 1-1 1A17 17 0 0 1 3 4a1 1 0 0 1 1-1h3.5a1 1 0 0 1 1 1c0 1.25.2 2.45.57 3.6a1 1 0 0 1-.25 1z"/></svg><span>555-014-7930</span></div>
      </div>
    </div>
  </div>
  <div class="footer-bottom">
    <div class="container">
      <span>© 2018 Calmridge Realty. All rights reserved.</span>
      <span class="follow">Follow Us On: <span></span><span></span><span></span><span></span></span>
    </div>
  </div>
</footer>

</body>
</html>
```